looking to have a web site for the company which provides services in the industrial and commercial sectors such as: electrical, automation control and system integration, construction and maintenance, millwright, equipment assembly repair and installation. I have the domain already brovinacorp.net and logo. Most recent projects fulfilled for the following clients: MeadowlarkFeeds, Calderwick University, ORIN, TALVIK, Ostmar, Northfield Grains

Target Market(s)

industrial and commercial sectors in electrical, automation, millwright and fabrication fields

Industry/Entity Type

Industrial

Coding

Coded - Design and coding required

Number of Pages Required

5+ page

Font styles to use
Sans Serif

Colors

Designer to choose colors to be used in the design.

Requirements
Nice to have
• looking to get something not complicated, nicely presented with minimum or no scrolling

```html
<!DOCTYPE html>
<html lang="en">
<head>
<meta charset="utf-8">
<title>BROVINA Corp — Industrial &amp; Commercial Services</title>
<link href="https://fonts.googleapis.com/css2?family=Fira+Sans:wght@300;400;600;700&display=swap" rel="stylesheet">
<style>
  :root {
    --ink: #000000;
    --teal-deep: #0b2a36;
    --teal-mid: #1a5a70;
    --teal-light: #2a7e98;
    --accent: #1a9fe0;
    --white: #ffffff;
    --text-soft: #e6eef2;
  }
  * { margin: 0; padding: 0; box-sizing: border-box; }
  html, body { width: 1200px; height: 675px; overflow: hidden; background: var(--ink); }
  body { font-family: "Fira Sans", Arial, sans-serif; color: var(--white); }

  .page { position: relative; width: 1200px; height: 675px; overflow: hidden; background: var(--ink); }

  .hero-visual {
    position: absolute; inset: 0;
    background:
      linear-gradient(90deg, var(--ink) 0%, var(--ink) 26%, rgba(0,0,0,0.55) 42%, rgba(0,0,0,0) 62%),
      linear-gradient(0deg, rgba(0,0,0,0.85) 0%, rgba(0,0,0,0) 35%),
      radial-gradient(ellipse at 90% 25%, var(--teal-light) 0%, var(--teal-mid) 35%, var(--teal-deep) 75%);
  }

  .brand {
    position: absolute; left: 18px; top: 20px;
    display: flex; align-items: center; gap: 8px;
    font-weight: 700; font-size: 20px; letter-spacing: 1px; color: var(--white);
  }
  .brand-mark { width: 12px; height: 12px; background: var(--accent); }

  .main-nav { position: absolute; top: 36px; left: 0; width: 100%; }
  .main-nav a {
    position: absolute; top: 0; font-weight: 600; font-size: 14px;
    color: var(--white); text-decoration: none; white-space: nowrap;
  }
  .main-nav a.is-active { color: var(--accent); }
  .main-nav a.is-active::after {
    content: ""; position: absolute; left: 0; right: 0; top: 28px;
    height: 1px; background: var(--accent);
  }

  .lang-switch { position: absolute; left: 1088px; top: 40px; font-size: 11px; font-weight: 600; }
  .lang-switch .is-current { color: var(--accent); }

  .title-rule { position: absolute; left: 0; top: 150px; width: 215px; height: 1px; background: var(--accent); }

  .hero-title { position: absolute; left: 235px; top: 122px; font-weight: 600; font-size: 46px; line-height: 54px; }
  .hero-title .line-two { display: block; padding-left: 120px; }

  .hero-lead {
    position: absolute; left: 355px; top: 240px; width: 430px;
    font-weight: 300; font-size: 15px; line-height: 22.5px; color: var(--text-soft);
  }

  .cta {
    position: absolute; left: 531px; top: 449px; width: 137px; height: 25px;
    border: 1px solid var(--accent); color: var(--accent);
    font-weight: 600; font-size: 14px; line-height: 23px; text-align: center; text-decoration: none;
  }

  .side-rule { position: absolute; left: 27px; top: 465px; width: 1px; height: 125px; background: var(--accent); }

  .social { position: absolute; left: 22px; top: 598px; list-style: none; }
  .social li { width: 10px; height: 10px; border-radius: 50%; background: var(--white); margin-bottom: 13px; }

  .footer-note { position: absolute; left: 0; width: 100%; top: 648px; text-align: center; font-size: 7px; color: var(--white); }
</style>
</head>
<body>
<div class="page">
  <div class="hero-visual" role="img" aria-label="Photograph of grain silos and an industrial elevator plant at dusk, tinted in deep teal"></div>

  <div class="brand"><span class="brand-mark"></span>BROVINA</div>

  <nav class="main-nav">
    <a class="is-active" href="#" style="left:333px">HOME</a>
    <a href="#" style="left:418px">WHO WE ARE</a>
    <a href="#" style="left:552px">WHAT WE DO</a>
    <a href="#" style="left:685px;top:-1px">PROJECTS</a>
    <a href="#" style="left:797px">CONTACTS</a>
  </nav>

  <div class="lang-switch">RU <span class="is-current">EN</span></div>

  <div class="title-rule"></div>
  <h1 class="hero-title">BROVINA<span class="line-two">Corp</span></h1>

  <p class="hero-lead">Company which provides services in the industrial and commercial sectors such as: electrical, automation control and system integration, construction and maintenance, millwright, equipment assembly repair and installation</p>

  <a class="cta" href="#">OUR PROJECTS</a>

  <div class="side-rule"></div>
  <ul class="social" aria-label="Social links">
    <li></li><li></li><li></li>
  </ul>

  <p class="footer-note">BROVINA Corp ©2017</p>
</div>
</body>
</html>
```